Create a pitch deck for a specialist physical product development search firm

Please review the attached project brief and the following instructions.
I need a designer to create a 10-slide pitch deck for Velmo, a specialist recruitment partner for physical product design & development companies. The deck will be used to pitch our retained/exclusive recruitment service to potential clients.
The design should:
Follow our bold, clean brand guidelines (provided)
Feel premium, minimalist, and professional
The deck includes:
Problem statement
Our story & differentiators
Process overview
2 client case studies
Social proof/testimonials
Clear call-to-action
Deliverables:
Editable Canva file (preferred) or PowerPoint
Exported PDF
Optional: Network carousel adaptation

```html
<!DOCTYPE html>
<html lang="en">
<head>
<meta charset="utf-8">
<title>Velmo pitch deck</title>
<link href="https://fonts.googleapis.com/css2?family=Poppins:wght@300;400;500;600;700&display=swap" rel="stylesheet">
<style>
:root{
  --stage:#553807;
  --white:#ffffff;
  --ink:#1d1d1b;
  --muted:#4a4a4a;
  --orange:#E8A23A;
  --orange-deep:#D98A0B;
  --orange-soft:#F3BA4C;
  --orange-pale:#F7D488;
  --panel:#F0F0F0;
  --line:#C9C9C9;
}
*{box-sizing:border-box;margin:0;padding:0}
html,body{width:1200px;height:975px;overflow:hidden;background:var(--stage)}
body{font-family:'Poppins',sans-serif;color:var(--ink);position:relative}
.slide{position:absolute;width:375px;height:211px;background:var(--white);overflow:hidden}
.c1{left:23px}.c2{left:411px}.c3{left:802px}
.r1{top:40px}.r2{top:268px}.r3{top:496px}.r4{top:724px}
.abs{position:absolute}
.h2{font-size:14px;font-weight:600;line-height:1.15}
.tiny{font-size:5.4px;line-height:1.35;color:var(--muted)}
.small{font-size:6px;line-height:1.35;color:var(--muted)}
ul.dots{list-style:none}
ul.dots li{position:relative;padding-left:10px;margin-bottom:2.5px}
ul.dots li::before{content:"";position:absolute;left:1px;top:2.4px;width:2.6px;height:2.6px;border-radius:50%;background:var(--orange)}
.brand{display:flex;align-items:center;gap:4px;font-weight:600}
.brand .sq{background:var(--orange)}
.foot-band{position:absolute;left:0;right:0;bottom:0;height:13px;background:#FBF4E6}
.foot-brand{position:absolute;right:18px;bottom:4px;font-size:7px}
.foot-brand .sq{width:5px;height:5px}
.pagenum{position:absolute;left:22px;bottom:4px;font-size:4px;color:#aaa}
.photo{position:absolute;border-radius:50%;background:radial-gradient(circle at 50% 40%,#9a9a9a,#3e3e3e)}
.title-main{position:absolute;left:0;right:0;text-align:center;line-height:1.1}
.case-title{left:25px;top:16px;text-align:center;width:48px}
.badge{position:absolute;left:22px;top:57px;width:50px;height:50px}
.stem{position:absolute;left:46.5px;top:106px;width:1px;height:82px;background:var(--line)}
.dome{position:absolute;left:26px;top:188px;width:42px;height:42px;border-radius:50%;background:linear-gradient(#e2e2e2,#fff)}
.client-name{font-size:13px;font-weight:600;color:#3a3f6b}
.role-line{font-size:9.5px;font-weight:600;line-height:1.2}
.role-line span{color:var(--orange-deep);display:block}
.solution{position:absolute;left:187px;top:106px;width:188px;height:73px;background:var(--orange-deep);padding:9px 10px;color:#fff}
.solution b{font-size:6px;font-weight:500;display:block;margin-bottom:3px}
.solution ul li{font-size:5.6px;line-height:1.3;color:#fff;margin-bottom:2px}
.solution ul li::before{background:#fff}
.challenges b{font-size:6px;font-weight:500;display:block;margin-bottom:3px;color:var(--ink)}
.pill-head{position:absolute;top:57px;height:13px;width:96px;background:var(--orange-soft);border-radius:0 6px 0 6px;font-size:5.6px;font-weight:600;padding:3px 6px}
.strip{position:absolute;left:22px;top:139px;width:333px;height:33px;background:var(--panel);border-radius:16px;display:flex;overflow:hidden}
.strip div{flex:1;display:flex;align-items:center;justify-content:center;font-size:7px;font-weight:600;border-right:1px solid #fff;color:#3a3f6b}
.icon-dot{position:absolute;width:24px;height:24px;border-radius:50%;background:var(--orange)}
.stat{position:absolute;color:#fff;text-align:center;line-height:1.15}
.stat .num{font-size:11px;font-weight:600;line-height:1.2}
.sum-pill{position:absolute;width:155px;height:36px;background:var(--panel);border-radius:0 18px 18px 0;font-size:6px;font-weight:600;display:flex;align-items:center;justify-content:center;padding-left:36px;text-align:center;line-height:1.3}
.sum-ring{position:absolute;left:-2px;top:0;width:36px;height:36px;border-radius:50%;background:var(--orange-deep)}
.sum-ring::after{content:"";position:absolute;left:6px;top:6px;width:24px;height:24px;border-radius:50%;background:#fff;border:1px solid var(--orange)}
.quote-text{position:absolute;left:201px;width:170px;font-size:4.8px;line-height:1.4;color:var(--muted)}
.quote-text b{display:block;color:var(--ink);font-weight:600;margin-top:2px;font-size:5px}
.contact-row{position:absolute;left:16px;display:flex;align-items:center;gap:7px;color:#fff;font-size:7.5px;font-weight:600;line-height:1.25}
.contact-ico{width:28px;height:28px;border-radius:50%;background:#fff;display:flex;align-items:center;justify-content:center}
</style>
</head>
<body>

<!-- Slide 1: light title -->
<section class="slide c1 r1" aria-label="Title slide, light">
  <div class="abs brand" style="left:149px;top:35px;font-size:19px"><span class="sq" style="width:13px;height:13px"></span>Velmo</div>
  <h1 class="title-main" style="top:92px;font-size:23px;font-weight:600">Presentation title here</h1>
  <p class="title-main" style="top:124px;font-size:9px">Subtitle here</p>
  <p class="title-main" style="top:173px;font-size:7px">Date</p>
</section>

<!-- Slide 2: orange title -->
<section class="slide c2 r1" aria-label="Title slide, orange" style="background:linear-gradient(90deg,#C27E0D,#E39A22)">
  <div class="abs" role="img" aria-label="Geometric brand pattern" style="left:0;top:0;width:160px;height:211px;background:linear-gradient(135deg,#B9780C,#CB8614)"></div>
  <div class="abs brand" style="left:187px;top:34px;font-size:19px;color:var(--ink)"><span class="sq" style="width:13px;height:13px;background:var(--orange-pale)"></span>Velmo</div>
  <h1 class="abs" style="left:187px;top:84px;font-size:19px;font-weight:600;color:#fff;line-height:1.2">Presentation<br>title here</h1>
  <p class="abs" style="left:187px;top:143px;font-size:7.5px;color:#fff">Subtitle here</p>
  <p class="abs" style="left:187px;top:172px;font-size:5px;color:#fff">Date</p>
</section>

<!-- Slide 3: introduction -->
<section class="slide c3 r1" aria-label="Introduction">
  <div class="abs" style="left:144px;top:0;width:231px;height:158px;background:var(--panel);border-radius:0 0 0 30px"></div>
  <h2 class="abs h2" style="left:22px;top:19px">Introduction</h2>
  <p class="abs small" style="left:23px;top:38px">Founded Velmo in January 2024</p>
  <div class="abs" style="left:41px;top:146px;width:90px;height:45px;background:var(--orange-deep);border-radius:24px 0 0 0"></div>
  <div class="photo" role="img" aria-label="Portrait photo of the founder" style="left:20px;top:58px;width:100px;height:100px;border:1px solid var(--orange-pale)"></div>
  <p class="abs" style="left:41px;top:163px;width:90px;text-align:center;color:#fff;font-size:9px;font-weight:600;line-height:1.1">Dan Ferrow<br><span style="font-size:6.5px;font-weight:400">Founder</span></p>
  <div class="abs" style="left:166px;top:20px"><div style="font-size:11px;font-weight:600">11+</div><p class="tiny" style="width:60px">years in product development recruitment</p></div>
  <div class="abs" style="left:166px;top:67px"><div style="font-size:11px;font-weight:600">350</div><p class="tiny" style="width:60px">design &amp; engineering placements</p></div>
  <div class="abs" style="left:166px;top:106px"><div style="font-size:11px;font-weight:600">14,000+</div><p class="tiny" style="width:70px">Network connections and followers in product design and engineering</p></div>
  <div class="abs" style="left:258px;top:21px;font-size:5.4px;line-height:1.3;color:var(--muted)">Exclusively focused on<br><b style="font-size:7.5px;color:var(--ink);font-weight:600">physical product<br>design &amp; development</b><br>(no apps!)</div>
  <div class="abs" style="left:258px;top:66px"><p style="font-size:7.5px;font-weight:600;line-height:1.2;margin-bottom:4px">Planet and people<br>friendly technology</p>
    <ul class="dots tiny"><li>Medical devices</li><li>Life sciences</li><li>Fem tech</li><li>Consumer technology</li><li>Consumer healthcare</li><li>Design Consultancy</li></ul></div>
  <p class="abs small" style="left:165px;top:161px;width:170px">Covering <b style="color:var(--ink);font-weight:600">Industrial Design, R&amp;D</b> &amp; <b style="color:var(--ink);font-weight:600">Mechanical Engineering</b> from mid-level through to C-Suite (<b style="color:var(--ink);font-weight:600">CTO</b>, <b style="color:var(--ink);font-weight:600">CDO</b> or <b style="color:var(--ink);font-weight:600">CPO</b>)</p>
  <div class="foot-band" role="img" aria-label="Faint brand pattern band"></div>
  <span class="pagenum">3</span>
  <div class="foot-brand brand"><span class="sq"></span>Velmo</div>
</section>

<!-- Slide 4: typical client profile -->
<section class="slide c1 r2" aria-label="Typical client profile">
  <h2 class="abs h2" style="left:22px;top:20px">Typical Client Profile</h2>
  <div class="pill-head" style="left:22px">Companies we help:</div>
  <div class="pill-head" style="left:141px">Typical challenges:</div>
  <div class="pill-head" style="left:259px">Desired outcomes:</div>
  <ul class="abs dots small" style="left:27px;top:77px;width:100px"><li>Physical product/ hardware firms</li><li>Hardware focused design consultancies</li></ul>
  <ul class="abs dots small" style="left:146px;top:77px;width:100px"><li>Limited employer brand reach / awareness</li><li>Limited recruitment resources / bandwidth</li><li>Protracted hiring cycles of 3 months+</li></ul>
  <ul class="abs dots small" style="left:264px;top:77px;width:100px"><li>Attract high-quality candidates from/ ahead of competition</li><li>Reduce time spent on recruitment process</li></ul>
  <div class="strip"><div>Lumeo</div><div style="background:#fff;"><span style="background:#111;color:#fff;padding:3px 5px;font-size:6.5px">Norvik</span></div><div style="font-size:6px">Talvo Studio</div><div>Brevan</div><div style="font-size:6px">Plainform</div><div style="color:#1e5bd6">Marlo</div></div>
  <div class="foot-band" role="img" aria-label="Faint brand pattern band"></div>
  <span class="pagenum">4</span>
  <div class="foot-brand brand"><span class="sq"></span>Velmo</div>
</section>

<!-- Slide 5: our solution -->
<section class="slide c2 r2" aria-label="Our solution">
  <h2 class="abs h2" style="left:22px;top:20px">Our Solution</h2>
  <div class="icon-dot" style="left:22px;top:46px"></div>
  <p class="abs tiny" style="left:50px;top:47px;width:58px;color:var(--ink)">Access to exclusive, vetted, high-quality talent - fast</p>
  <div class="icon-dot" style="left:110px;top:46px"></div>
  <p class="abs tiny" style="left:138px;top:51px;width:55px;color:var(--ink)">Expert knowledge of the market</p>
  <div class="icon-dot" style="left:22px;top:80px"></div>
  <p class="abs tiny" style="left:50px;top:80px;width:58px;color:var(--ink)">Huge proprietary network (CRM &amp; social media connections / followers)</p>
  <div class="icon-dot" style="left:110px;top:80px"></div>
  <p class="abs tiny" style="left:138px;top:80px;width:58px;color:var(--ink)">Expert knowledge of pitching/selling roles – engaging hard-to-reach candidates</p>
  <div class="stat" style="left:22px;top:118px;width:58px;height:34px;background:var(--orange-deep);border-radius:14px 0 0 0;padding-top:7px"><div class="num">100%</div><div style="font-size:4.8px">Fill Rate</div></div>
  <div class="stat" style="left:80px;top:118px;width:67px;height:34px;background:var(--orange-soft);border-radius:0 14px 0 0;padding-top:4px"><div class="num">+91</div><div style="font-size:4.5px">All-time Net Promoter<br>Score (NPS)</div></div>
  <div class="stat" style="left:80px;top:152px;width:83px;height:35px;background:var(--orange-deep);border-radius:0 0 14px 0;padding-top:3px"><div class="num">97%</div><div style="font-size:5px;font-weight:600">Retention Rate</div><div style="font-size:3.6px">(candidate still employed<br>after 12 months)</div></div>
  <div class="abs" role="img" aria-label="Diagram of the candidate market by activity and desperation" style="left:198px;top:44px;width:160px;height:135px;background:linear-gradient(180deg,#F3B845,#F7E2B4)"></div>
  <div class="foot-band" role="img" aria-label="Faint brand pattern band"></div>
  <span class="pagenum">5</span>
  <div class="foot-brand brand"><span class="sq"></span>Velmo</div>
</section>

<!-- Slide 6: case study 1 -->
<section class="slide c3 r2" aria-label="Case study 1">
  <h2 class="abs h2 case-title" style="left:25px;width:50px">Case Study</h2>
  <svg class="badge" viewBox="0 0 50 50" aria-hidden="true"><path d="M0 0 H18 V14 H32 V0 H50 V25 A25 25 0 0 1 0 25 Z" fill="#F3B845"/><circle cx="25" cy="25" r="17" fill="#E39A22"/><circle cx="25" cy="25" r="13" fill="#fff"/><text x="25" y="31" text-anchor="middle" font-family="Poppins,sans-serif" font-size="17" font-weight="600" fill="#1d1d1b">1</text></svg>
  <div class="stem"></div><div class="dome"></div>
  <div class="abs brand client-name" style="left:84px;top:30px"><span style="width:9px;height:9px;border-radius:50%;background:#e4567a"></span>Lumeo</div>
  <p class="abs role-line" style="left:83px;top:65px">Lumeo Health<span>Chief Product Officer</span></p>
  <div class="abs challenges" style="left:198px;top:38px"><b>Challenges:</b>
    <ul class="dots small"><li>Recent changes in senior leadership</li><li>Unsettled staff</li><li>Absent founder</li><li>Lack of trust in recruiters</li><li>Limited budget</li></ul></div>
  <div class="solution" style="top:105px"><b>Solution:</b>
    <ul class="dots"><li>Designed a transparent process to engage the right candidates</li><li>4 candidates presented and interviewed</li><li>1 offer made and accepted within 4.5 weeks of engagement</li></ul></div>
  <div class="foot-band" role="img" aria-label="Faint brand pattern band"></div>
  <span class="pagenum">6</span>
  <div class="foot-brand brand"><span class="sq"></span>Velmo</div>
</section>

<!-- Slide 7: case study 2 -->
<section class="slide c1 r3" aria-label="Case study 2">
  <h2 class="abs h2 case-title" style="left:22px;width:50px">Case Study</h2>
  <svg class="badge" viewBox="0 0 50 50" aria-hidden="true"><path d="M0 0 H18 V14 H32 V0 H50 V25 A25 25 0 0 1 0 25 Z" fill="#F3B845"/><circle cx="25" cy="25" r="17" fill="#E39A22"/><circle cx="25" cy="25" r="13" fill="#fff"/><text x="25" y="31" text-anchor="middle" font-family="Poppins,sans-serif" font-size="17" font-weight="600" fill="#1d1d1b">2</text></svg>
  <div class="stem"></div><div class="dome"></div>
  <div class="abs brand client-name" style="left:83px;top:28px;color:#2e4a8c">Plainform<span style="width:9px;height:9px;border-radius:50%;border:1px solid #2e4a8c;background:none;margin-left:2px"></span></div>
  <p class="abs role-line" style="left:83px;top:65px">Plainform Works<span>Technical Lead</span></p>
  <div class="abs challenges" style="left:198px;top:40px"><b>Challenges:</b>
    <ul class="dots small"><li>New studio location</li><li>Challenging location</li><li>Very specific skills and experience requirements</li><li>Limited employer brand awareness</li><li>Limited recruitment bandwidth</li></ul></div>
  <div class="solution" style="left:188px"><b>Solution:</b>
    <ul class="dots"><li>Designed a tailored process</li><li>3 candidates presented and interviewed</li><li>1 offer made and accepted within 6 weeks of engagement</li></ul></div>
  <div class="foot-band" role="img" aria-label="Faint brand pattern band"></div>
  <span class="pagenum">7</span>
  <div class="foot-brand brand"><span class="sq"></span>Velmo</div>
</section>

<!-- Slide 8: case study 3 -->
<section class="slide c2 r3" aria-label="Case study 3">
  <h2 class="abs h2 case-title" style="left:22px;width:50px">Case Study</h2>
  <svg class="badge" viewBox="0 0 50 50" aria-hidden="true"><path d="M0 0 H18 V14 H32 V0 H50 V25 A25 25 0 0 1 0 25 Z" fill="#F3B845"/><circle cx="25" cy="25" r="17" fill="#E39A22"/><circle cx="25" cy="25" r="13" fill="#fff"/><text x="25" y="31" text-anchor="middle" font-family="Poppins,sans-serif" font-size="17" font-weight="600" fill="#1d1d1b">3</text></svg>
  <div class="stem"></div><div class="dome"></div>
  <div class="abs brand client-name" style="left:83px;top:36px;color:var(--ink)"><span style="width:9px;height:9px;border-radius:50%;background:#8cc63f"></span>Brevan</div>
  <p class="abs role-line" style="left:83px;top:65px">Brevan<span>Principal Mechanical<br>Engineer</span></p>
  <div class="abs challenges" style="left:198px;top:40px"><b>Challenges:</b>
    <ul class="dots small"><li>Previously took 9+ months to hire</li><li>Multiple candidates dropped out</li><li>Recruiters failed to find suitable talent</li><li>Limited employer brand awareness</li><li>Limited recruitment resources</li></ul></div>
  <div class="solution" style="left:187px;height:80px"><b>Solution:</b>
    <ul class="dots"><li>Designed a transparent process to account for stakeholder availability</li><li>Utilised Brevan's pitch deck to drive engagement</li><li>4 candidates presented and interviewed</li><li>1 offer made and accepted within 3 weeks of engagement</li></ul></div>
  <div class="foot-band" role="img" aria-label="Faint brand pattern band"></div>
  <span class="pagenum">8</span>
  <div class="foot-brand brand"><span class="sq"></span>Velmo</div>
</section>

<!-- Slide 9: engagement structure -->
<section class="slide c3 r3" aria-label="Engagement structure">
  <h2 class="abs h2" style="left:22px;top:18px">Engagement<br>Structure</h2>
  <ul class="abs dots tiny" style="left:22px;top:56px;width:118px"><li>We work on an exclusive search model</li><li>Allows us to make you our highest priority</li><li>In-depth candidate vetting process</li><li>Clarity and consistency of your brand</li><li>100% of candidates exclusive to you</li><li>Fully refundable up-front engagement fee, deducted from the final fee (no extra costs)</li><li>Guaranteed completion</li><li>Extended post-placement protection</li></ul>
  <svg class="abs" style="left:155px;top:40px" width="205" height="145" viewBox="0 0 205 145" role="img" aria-label="Five-stage engagement process diagram">
    <rect x="3" y="45" width="192" height="54" rx="27" fill="#EDEDED"/>
    <g stroke="#bbb" stroke-width=".5"><line x1="20" y1="12" x2="20" y2="45"/><line x1="77" y1="12" x2="77" y2="45"/><line x1="133" y1="12" x2="133" y2="45"/><line x1="178" y1="12" x2="178" y2="45"/><line x1="47" y1="99" x2="47" y2="125"/><line x1="102" y1="99" x2="102" y2="125"/><line x1="157" y1="99" x2="157" y2="125"/></g>
    <path d="M30 45 A27 27 0 0 0 3 72 H30 Z" fill="#E39A22"/><path d="M3 72 A27 27 0 0 0 30 99 V72 Z" fill="#F3B845"/>
    <path d="M58 45 A27 27 0 0 1 85 72 H58 Z" fill="#F3B845"/>
    <path d="M33 72 H58 V99 A26 26 0 0 1 33 72 Z" fill="#E39A22"/>
    <path d="M113 45 A27 27 0 0 0 86 72 H113 Z" fill="#F3B845"/>
    <path d="M86 72 H113 V99 A27 27 0 0 1 86 72 Z" fill="#F3B845" opacity=".7"/>
    <path d="M116 72 H140 V45 A27 27 0 0 1 116 72 Z" fill="#E39A22" opacity=".9"/>
    <path d="M143 72 H168 V99 A26 26 0 0 1 143 72 Z" fill="#E39A22"/>
    <path d="M168 45 A27 27 0 0 1 195 72 H168 Z" fill="#E39A22"/><path d="M195 72 A27 27 0 0 1 168 99 V72 Z" fill="#F3B845"/>
    <g font-family="Poppins,sans-serif" font-size="5" font-weight="600" fill="#1d1d1b" text-anchor="middle">
      <text x="20" y="4">Qualify</text><text x="20" y="10">Role</text>
      <text x="77" y="4">Research</text><text x="77" y="10">Phase</text>
      <text x="133" y="7">Interviews</text><text x="178" y="7">Onboarding</text>
      <text x="47" y="130">Agree</text><text x="47" y="136">Candidate</text><text x="47" y="142">Briefing</text>
      <text x="102" y="130">Shortlist</text><text x="102" y="136">Agreement</text>
      <text x="157" y="130">Offer</text><text x="157" y="136">Management</text>
      <text x="24" y="52">01</text><text x="63" y="52">03</text><text x="119" y="52">05</text><text x="174" y="52">05</text>
      <text x="38" y="97">02</text><text x="93" y="97">04</text><text x="148" y="97">05</text>
    </g>
  </svg>
  <div class="foot-band" role="img" aria-label="Faint brand pattern band"></div>
  <span class="pagenum">9</span>
  <div class="foot-brand brand"><span class="sq"></span>Velmo</div>
</section>

<!-- Slide 10: feedback -->
<section class="slide c1 r4" aria-label="Feedback">
  <h2 class="abs h2" style="left:22px;top:18px">Feedback</h2>
  <p class="abs" style="left:22px;top:42px;font-size:8px;font-weight:600">Net Promoter Score (NPS)</p>
  <p class="abs small" style="left:22px;top:56px;width:85px">The universally recognised way of measuring customer satisfaction and loyalty</p>
  <svg class="abs" style="left:18px;top:105px" width="100" height="65" viewBox="0 0 100 65" role="img" aria-label="NPS gauge showing +91">
    <defs><linearGradient id="gaugeArc" x1="0" x2="1"><stop offset="0" stop-color="#e8306d"/><stop offset=".6" stop-color="#f3a43b"/><stop offset="1" stop-color="#2bb673"/></linearGradient></defs>
    <path d="M12 44 A38 38 0 0 1 88 44" fill="none" stroke="url(#gaugeArc)" stroke-width="3" stroke-linecap="round"/>
    <line x1="52" y1="44" x2="86" y2="36" stroke="#1d1d1b" stroke-width="2" stroke-linecap="round"/>
    <circle cx="52" cy="44" r="3" fill="#1d1d1b"/>
    <text x="62" y="30" transform="rotate(-22 62 30)" font-family="Poppins,sans-serif" font-size="7" fill="#333">Goal</text>
    <g font-family="Poppins,sans-serif" font-size="6" fill="#333" text-anchor="middle"><text x="10" y="57">-100</text><text x="52" y="56" font-weight="600">+91</text><text x="90" y="57">+100</text></g>
  </svg>
  <p class="abs tiny" style="left:22px;top:182px;font-size:4.4px;width:110px">Above +80 NPS is considered World Class<br>Recruitment industry avg NPS is +30</p>
  <div class="photo" role="img" aria-label="Portrait photo of client testimonial" style="left:148px;top:24px;width:45px;height:45px"></div>
  <p class="quote-text" style="top:27px">Velmo made hiring seamless. They didn't just find us the right Chief Product Officer—they helped us define what we needed. The structured, pre-planned process saved us time and stress. Compared to other recruiters, this was faster, more personalised, and highly organised. The result? We now have a product ready for market. That says it all.<b>Ruth Alder, CEO &amp; Co-Founder – Lumeo Health</b></p>
  <div class="photo" role="img" aria-label="Portrait photo of client testimonial" style="left:148px;top:83px;width:45px;height:45px"></div>
  <p class="quote-text" style="top:89px">Good advice from Dan. Four good candidates, no bad ones. No agency shenanigans, helped us build a professional hiring experience.<b>Owen Preece, Co-Founder – Gauge Works</b></p>
  <div class="photo" role="img" aria-label="Portrait photo of client testimonial" style="left:148px;top:137px;width:45px;height:45px"></div>
  <p class="quote-text" style="top:142px">We spent a lot less time than normal needing to review CV's and screen candidates as the 4 CV's and candidates we got were all excellent. Made an offer 2 days after interviewing one of the four.<b>Lewis Harne, Head of Engineering – Brevan</b></p>
  <div class="abs" style="left:332px;top:162px;font-size:28px;font-weight:700;color:#e6e6e6;line-height:1">”</div>
  <div class="foot-band" role="img" aria-label="Faint brand pattern band"></div>
  <span class="pagenum">10</span>
  <div class="foot-brand brand"><span class="sq"></span>Velmo</div>
</section>

<!-- Slide 11: summary -->
<section class="slide c2 r4" aria-label="Summary">
  <h2 class="abs h2" style="left:22px;top:18px">Summary</h2>
  <div class="sum-pill" style="left:18px;top:48px"><span class="sum-ring"></span>Robust, best practice search</div>
  <div class="sum-pill" style="left:200px;top:48px"><span class="sum-ring"></span>Guaranteed completion</div>
  <div class="sum-pill" style="left:18px;top:95px"><span class="sum-ring"></span>Exclusive candidates</div>
  <div class="sum-pill" style="left:200px;top:95px"><span class="sum-ring"></span>World-class customer experience</div>
  <div class="sum-pill" style="left:18px;top:142px"><span class="sum-ring"></span>6 weeks average<br>time-to-hire</div>
  <div class="sum-pill" style="left:200px;top:142px"><span class="sum-ring"></span>Fully refundable engagement fee, deducted from completion fee</div>
  <div class="foot-band" role="img" aria-label="Faint brand pattern band"></div>
  <span class="pagenum">11</span>
  <div class="foot-brand brand"><span class="sq"></span>Velmo</div>
</section>

<!-- Slide 12: call to action -->
<section class="slide c3 r4" aria-label="Call to action" style="background:var(--orange-soft)">
  <div class="abs" role="img" aria-label="Faint geometric brand pattern" style="inset:0;background:linear-gradient(135deg,#F0B444,#F6C25A)"></div>
  <div class="abs" style="left:0;top:150px;width:42px;height:61px;background:#fff;border-radius:0 14px 0 0"></div>
  <div class="abs" style="left:0;top:172px;width:375px;height:39px;background:var(--orange-deep);opacity:.35"></div>
  <h2 class="abs" style="left:52px;top:44px;font-size:27px;font-weight:600;color:#fff;line-height:1.25">Ready to<br>hire?<br>Let’s talk.</h2>
  <div class="abs" style="left:200px;top:18px;width:175px;height:153px;background:#E9A22E;border-radius:22px 0 0 0"></div>
  <div class="contact-row" style="left:216px;top:36px"><span class="contact-ico"><svg width="12" height="10" viewBox="0 0 12 10"><rect x="1.5" y="1" width="9" height="6" fill="none" stroke="#555" stroke-width=".8"/><line x1="0" y1="8.5" x2="12" y2="8.5" stroke="#555" stroke-width=".8"/></svg></span>www.velmotalent.com</div>
  <div class="contact-row" style="left:216px;top:74px"><span class="contact-ico"><svg width="12" height="12" viewBox="0 0 12 12"><path d="M3 1 L5 4 L4 5 Q5 7.5 7 8 L8 7 L11 9 L10 11 Q2 10 1 2 Z" fill="#555"/></svg></span>+1 (555) 014 2270<br>+44 (0) 20 7946 0312</div>
  <div class="contact-row" style="left:216px;top:112px"><span class="contact-ico"><svg width="12" height="10" viewBox="0 0 12 10"><rect x=".5" y=".5" width="11" height="9" fill="none" stroke="#555" stroke-width=".8"/><path d="M.5 .5 L6 5.5 L11.5 .5" fill="none" stroke="#555" stroke-width=".8"/></svg></span>dan@velmotalent.com</div>
  <div class="abs" style="left:200px;top:150px;width:175px;height:31px;background:#fff;border-radius:0 0 0 14px"></div>
  <div class="abs brand" style="left:218px;top:154px;font-size:18px;color:var(--ink)"><span class="sq" style="width:13px;height:13px"></span>Velmo</div>
</section>

</body>
</html>
```